Digital Album Cover - Where The Quiet River Bends (Piano & Cello)

HiI would like a digital album coverTitle: "Where The Quiet River Bends (Piano & Cello)"Artist: "Lorcan Pettigrew & The Oduya Priscilla"

• Original creativity
• Copyrighted images

```html
<!DOCTYPE html>
<html lang="en">
<head>
<meta charset="utf-8">
<title>Where The Quiet River Bends (Piano &amp; Cello) — Lorcan Pettigrew &amp; The Oduya Priscilla</title>
<link rel="stylesheet" href="https://fonts.googleapis.com/css2?family=Pinyon+Script&display=swap">
<style>
  :root {
    --crimson-deep: #6e0606;
    --crimson: #a30a08;
    --crimson-bright: #c4160c;
    --ember: #8a2a10;
    --amber-glow: #c58a3a;
    --umber: #3a1a0a;
    --olive-shadow: #4a3e1a;
    --title-gold: #c99a5e;
  }
  html, body {
    margin: 0;
    padding: 0;
    overflow: hidden;
    background: var(--crimson-deep);
  }
  .cover {
    position: relative;
    width: 1200px;
    height: 1188px;
    overflow: hidden;
    background: var(--crimson);
  }
  .band {
    position: absolute;
    left: 0;
    width: 1200px;
  }
  .band--top {
    top: 0;
    height: 136px;
    background: linear-gradient(90deg, var(--crimson) 0%, #b20d0a 45%, var(--crimson) 100%);
  }
  .band--bottom {
    top: 984px;
    height: 204px;
    background: linear-gradient(180deg, #9c0e0a 0%, var(--crimson) 50%, #8e0c09 100%);
  }
  .collage {
    position: absolute;
    left: 0;
    top: 136px;
    width: 1200px;
    height: 848px;
    background:
      radial-gradient(ellipse 260px 300px at 830px 560px, var(--amber-glow) 0%, rgba(197,138,58,0.55) 45%, rgba(197,138,58,0) 100%),
      radial-gradient(ellipse 200px 320px at 270px 560px, var(--olive-shadow) 0%, rgba(74,62,26,0) 100%),
      linear-gradient(180deg, rgba(0,0,0,0) 0%, rgba(0,0,0,0) 55%, rgba(40,8,4,0.55) 100%),
      linear-gradient(90deg, var(--ember) 0%, var(--crimson) 30%, var(--crimson-bright) 60%, var(--crimson) 85%, var(--umber) 100%);
  }
  .title, .artist {
    position: absolute;
    left: 0;
    top: 0;
    margin: 0;
    font-family: "Pinyon Script", cursive;
    font-weight: 400;
    color: var(--title-gold);
    line-height: 1;
  }
  .title { font-size: 90px; }
  .title span, .artist {
    position: absolute;
    white-space: nowrap;
  }
  .title .line-1 { left: 189px; top: 388px; }
  .title .line-2 { left: 211px; top: 530px; }
  .title .line-3 { left: 205px; top: 673px; }
  .artist {
    left: 210px;
    top: 800px;
    font-size: 36px;
  }
</style>
</head>
<body>
  <main class="cover">
    <div class="band band--top"></div>
    <div class="collage" role="img" aria-label="Layered red and amber collage of a cello body with strings and f-holes over textured abstract shapes"></div>
    <div class="band band--bottom"></div>
    <h1 class="title">
      <span class="line-1">where the quiet</span>
      <span class="line-2">river bends</span>
      <span class="line-3">(piano &amp; cello)</span>
    </h1>
    <p class="artist">Lorcan Pettigrew &amp; The Oduya Priscilla</p>
  </main>
</body>
</html>
```